Redesign of a Reputation Management Website

StandingMend.com Requirement Doc
Reference Site: NameHarbor.com (should NOT copy this site but be patterned in a similar way because we are changing the back end and functionality similar to it)
StandingMend.com is a functional active site that needs a redesign.
FRONT END
Landing / Home Page:
• Should be built with WordPress for ease of use
• Should contain high quality imagery
• Should contain logo
• Should contain Navigation links on top right or top center
1. Personal
2. Business
3. About us
4. Account Login
5. Sign Up
• Should be broken into sections
1. Header – High Quality Image/Slider/Social Media Icons/Contact Info
2. Information
3. Services Personal / Business
4. Sign Up
5. Footer – Links/Contacts/ Social media
6. Sub footer- Info Links
Landing / Home Page Colours:
Main colours should be contrasting light and dark blues like #1A9BFC, #31A5FC and #60BAF7, with minimal green like #77AE00 as an accent colour. The footer and sub footer should be #1C3344
Landing / Home Functional Requirements:
All front end links should link out their individual pages and/or back end processes, this includes navigation menu items, footer links, and sign up and social media buttons. All linked pages should contain I quality information, Graphics, calls to action and sign up options.
Sign up should have two options, Sign up with social media accounts or standard sign up form.
Login should have two options, Login with social media accounts or standard login form.
Target Market(s)
People that are looking to manage their reputation or repair it, or manage their brand, monitor their reputation online
Industry/Entity Type
Management
Number of Pages Required
1 page
Look and feel

```html
<!DOCTYPE html>
<html lang="en">
<head>
<meta charset="utf-8">
<title>Standing Mend – Control &amp; Protect Your Online Reputation</title>
<link href="https://fonts.googleapis.com/css2?family=Questrial&family=Open+Sans:wght@400;600;700&display=swap" rel="stylesheet">
<style>
:root{
  --blue:#1A9BFC;
  --blue-2:#31A5FC;
  --blue-3:#60BAF7;
  --green:#77AE00;
  --navy:#1C3344;
  --navy-line:#2c4658;
  --ink:#222;
  --text:#555;
  --muted:#8a8f94;
  --white:#fff;
  --hub:#3b5a99;
  --chirp:#3fb6ea;
  --heading:"Questrial",sans-serif;
  --body:"Open Sans",sans-serif;
}
*{box-sizing:border-box;margin:0;padding:0}
html,body{width:1200px;height:2642px;overflow:hidden}
body{font-family:var(--body);color:var(--text);background:var(--white);position:relative}
a{color:inherit;text-decoration:none}
.abs{position:absolute}

/* Hero */
.hero{position:absolute;left:0;top:0;width:1200px;height:675px;
  background:linear-gradient(100deg,#2a3038 0%,#4d5660 35%,#8f98a0 60%,#5d6670 80%,#3a4048 100%);overflow:hidden}
.hero-photo{position:absolute;inset:0;background:
  radial-gradient(ellipse 260px 330px at 640px 220px,rgba(190,170,150,.45),transparent 70%),
  radial-gradient(ellipse 300px 360px at 880px 180px,rgba(200,180,160,.4),transparent 70%),
  linear-gradient(180deg,rgba(20,26,34,.15),rgba(20,26,34,.45))}
.brand{left:75px;top:18px;color:var(--white);display:flex;align-items:center;gap:10px}
.brand-mark{width:40px;height:40px;background:var(--white);opacity:.9}
.brand-name{font-family:var(--heading);font-size:30px;line-height:1}
.brand-tag{left:128px;top:62px;color:#dfe6ec;font-size:14px;font-family:var(--heading)}
.nav{right:75px;top:38px;display:flex;align-items:center;gap:24px;color:var(--white);font-size:14px;font-family:var(--heading)}
.nav .btn-outline{border:1px solid var(--white);padding:5px 10px}
.hero-title{left:73px;top:228px;color:var(--white);font-family:var(--heading);font-size:38px;line-height:40px;letter-spacing:.5px;font-weight:700}
.hero-sub{left:73px;top:318px;color:#eef2f5;font-family:var(--heading);font-size:21px;line-height:24px}
.hero-label{color:var(--white);font-family:var(--heading);font-size:13px;font-weight:700;letter-spacing:.3px}
.social-tile{width:84px;height:84px;color:var(--white);font-size:12px;font-weight:600;display:flex;flex-direction:column;align-items:center;justify-content:flex-end;padding-bottom:10px;gap:12px}
.social-tile .dot{width:34px;height:34px;border-radius:50%;background:rgba(255,255,255,.85)}
.tile-hub{left:73px;top:455px;background:var(--hub)}
.tile-chirp{left:165px;top:455px;background:var(--chirp)}
.tile-mail{left:288px;top:455px;background:var(--green)}
.hero-or{left:258px;top:488px;color:var(--white);font-family:var(--heading);font-size:14px}
.hero-divider{left:415px;top:430px;width:1px;height:110px;background:rgba(255,255,255,.4)}
.hero-phone{left:472px;top:468px;color:var(--white);font-family:var(--heading);font-size:29px;font-weight:700}
.hero-mail{left:482px;top:502px;color:#e6ecf0;font-size:16px}
.slider-dots{left:1088px;top:626px;display:flex;gap:6px}
.slider-dots span{width:8px;height:8px;border-radius:50%;background:rgba(255,255,255,.55)}
.slider-dots span:first-child{background:var(--white)}

/* Welcome */
.welcome-title{left:75px;top:727px;border-left:4px solid var(--blue);padding-left:10px;font-family:var(--heading);font-weight:700;font-size:28px;line-height:29px;color:var(--ink)}
.welcome-copy{left:73px;top:795px;width:510px;font-size:13.2px;line-height:22px;color:var(--text)}
.welcome-copy p+p{margin-top:22px}
.btn-ghost{left:73px;top:1063px;width:102px;height:32px;border:2px solid var(--blue-3);font-family:var(--heading);font-weight:700;font-size:12px;color:var(--ink);display:flex;align-items:center;justify-content:center}
.feature{left:610px;width:520px;height:130px}
.feature svg{position:absolute;left:0;top:0}
.feature h3{position:absolute;left:155px;top:0;font-family:var(--heading);font-size:16px;font-weight:700;color:var(--ink);letter-spacing:.3px}
.feature p{position:absolute;left:155px;top:30px;width:365px;font-size:13.2px;line-height:24px;color:var(--text)}
.feature p a{color:var(--blue)}

/* Services */
.services{position:absolute;left:0;top:1180px;width:1200px;height:608px;background:var(--blue)}
.section-title{width:1200px;text-align:center;font-family:var(--heading);font-weight:700;font-size:28px}
.services .section-title{top:52px;color:var(--white)}
.services-divider{left:600px;top:120px;width:1px;height:430px;background:rgba(255,255,255,.35)}
.service-card{top:125px;width:330px;height:415px;background:var(--white);border-radius:14px;box-shadow:0 4px 10px rgba(0,0,0,.15);overflow:visible}
.service-photo{height:250px;border-radius:14px 14px 0 0}
.photo-personal{background:linear-gradient(135deg,#dfe3e7,#c6cfd8 60%,#aeb9c4)}
.photo-business{background:linear-gradient(135deg,#cfe3f3,#9fb6ca 55%,#4c5c6e)}
.service-card h3{margin-top:22px;text-align:center;font-family:var(--heading);font-weight:700;font-size:17px;color:var(--ink)}
.service-card .rule{width:30px;height:3px;background:var(--blue-3);margin:12px auto}
.service-card p{padding:0 42px;text-align:center;font-size:13.2px;line-height:24px;color:var(--text)}
.service-card .btn-pill{position:absolute;left:100px;bottom:-16px;width:130px;height:32px;border-radius:16px;background:var(--blue-2);color:var(--white);font-family:var(--heading);font-weight:700;font-size:12px;display:flex;align-items:center;justify-content:center;box-shadow:0 2px 4px rgba(0,0,0,.2)}

/* Sign up */
.signup-title{top:1838px;color:var(--ink)}
.col-title{font-family:var(--heading);font-weight:700;font-size:15px;color:var(--ink);text-align:center}
.signup-divider{left:600px;top:1910px;width:1px;height:270px;background:#e3e6e9}
.signup-or{left:590px;top:2033px;font-family:var(--heading);font-weight:700;font-size:13px;color:var(--ink)}
.social-btn{left:202px;width:258px;height:38px;border-radius:3px;color:var(--white);font-size:15px;display:flex;align-items:center;padding:0 14px;gap:12px;box-shadow:0 2px 3px rgba(0,0,0,.2)}
.social-btn .arrow{margin-left:auto;font-weight:700}
.social-btn .sq{width:14px;height:14px;background:rgba(255,255,255,.85)}
.btn-hub{top:2026px;background:var(--hub)}
.btn-chirp{top:2079px;background:var(--chirp)}
.field{left:705px;width:332px;height:38px;border:1px solid #d6dadd;border-radius:3px;padding:0 12px;display:flex;align-items:center;font-size:13px;color:#9aa0a5}
.btn-create{left:705px;top:2124px;width:332px;height:48px;background:var(--green);color:var(--white);border-radius:3px;font-family:var(--heading);font-weight:700;font-size:14px;display:flex;align-items:center;justify-content:center;letter-spacing:.3px}
.terms{top:2216px;width:1200px;text-align:center;font-size:14px;color:var(--text)}
.terms a{color:var(--blue)}

/* Footer */
.footer{position:absolute;left:0;top:2288px;width:1200px;height:354px;background:var(--navy);color:#c6d0d8}
.footer h4{position:absolute;top:60px;font-family:var(--heading);font-weight:700;font-size:14px;color:var(--white);letter-spacing:.3px}
.footer ul{position:absolute;top:92px;list-style:none;font-size:13px;line-height:22px}
.contact{position:absolute;left:613px;display:flex;gap:14px;font-size:13px;line-height:19px}
.contact .ico{width:30px;height:30px;border-radius:50%;background:#3a5366;flex:none;display:flex;align-items:center;justify-content:center}
.follow{position:absolute;left:883px;display:flex;align-items:center;gap:10px;font-size:13px}
.follow .ring{width:26px;height:26px;border-radius:50%;border:1px solid #7e93a3}
.subfooter{position:absolute;left:0;top:307px;width:1200px;height:47px;border-top:1px solid var(--navy-line);font-size:12px;color:#aab6c0}
.subfooter .copy{position:absolute;left:73px;top:16px}
.subfooter nav{position:absolute;right:75px;top:16px;display:flex;gap:16px}
</style>
</head>
<body>

<header class="hero">
  <div class="hero-photo" role="img" aria-label="Two businessmen in suits reviewing documents at a desk"></div>
  <div class="abs brand"><span class="brand-mark"></span><span class="brand-name">Standing Mend</span></div>
  <div class="abs brand-tag">Reputation Consulting Since 1992</div>
  <nav class="abs nav">
    <a href="#">Personal</a><a href="#">Business</a><a href="#">About Us</a>
    <a href="#" class="btn-outline">Account Login</a><a href="#" class="btn-outline">Sign Up</a>
  </nav>
  <h1 class="abs hero-title">CONTROL &amp; PROTECT<br>YOUR ONLINE REPUTATION</h1>
  <p class="abs hero-sub">Ranked one of the worlds leading<br>internet reputation management specialists</p>
  <div class="abs hero-label" style="left:73px;top:428px">SIGN UP FOR FREE WITH:</div>
  <a class="abs social-tile tile-hub" href="#"><span class="dot"></span>SOCIALHUB</a>
  <a class="abs social-tile tile-chirp" href="#"><span class="dot"></span>CHIRPLINE</a>
  <span class="abs hero-or">OR</span>
  <a class="abs social-tile tile-mail" href="#">
    <svg width="38" height="30" viewBox="0 0 38 30"><rect x="1" y="3" width="36" height="25" fill="none" stroke="#fff" stroke-width="3"/><path d="M2 5 L19 18 L36 5" fill="none" stroke="#fff" stroke-width="3"/></svg>EMAIL</a>
  <div class="abs hero-divider"></div>
  <div class="abs hero-label" style="left:435px;top:428px">NEED TO HELP!</div>
  <svg class="abs" style="left:435px;top:472px" width="28" height="28" viewBox="0 0 28 28"><path d="M7 3 L11 9 L8 12 C10 16 12 18 16 20 L19 17 L25 21 L22 26 C12 25 3 16 2 6 Z" fill="none" stroke="#fff" stroke-width="2"/></svg>
  <div class="abs hero-phone">+1 888 555 0142</div>
  <div class="abs hero-mail">Hello@StandingMend.com</div>
  <div class="abs slider-dots"><span></span><span></span><span></span></div>
</header>

<section class="welcome">
  <h2 class="abs welcome-title">WELCOME TO<br>STANDING MEND</h2>
  <div class="abs welcome-copy">
    <p>StandingMend.com is one of the top reputation management agencies in the industry specializing in Personal Reputation Repair, Business Reputation Repair, Mugshot Removals, Expungements, and other removal packages. We offer our services to both local and international clients. Our dedicated team adopts a unique approach to controlling your online reputation.</p>
    <p>In recent years, the internet has emerged as the largest tool to find information about large brands, individuals or businesses. Maintaining a positive online reputation is no longer just a nice suggestion, it is crucial. We treat every client as if they were a member of our own family we are trying to protect.</p>
  </div>
  <a class="abs btn-ghost" href="#">READ MORE</a>

  <div class="abs feature" style="top:735px">
    <svg width="100" height="100" viewBox="0 0 100 100"><circle cx="40" cy="56" r="36" fill="none" stroke="#e6eaee" stroke-width="3"/><path d="M40 20 A36 36 0 0 1 76 56" fill="none" stroke="#1A9BFC" stroke-width="4"/><circle cx="40" cy="56" r="27" fill="#fff" stroke="#dde2e6"/><path d="M28 56 L37 65 L53 46" fill="none" stroke="#1C3344" stroke-width="5" stroke-linecap="round" stroke-linejoin="round"/><circle cx="76" cy="14" r="13" fill="#1A9BFC"/><text x="76" y="18.5" text-anchor="middle" font-family="Open Sans,sans-serif" font-size="12" font-weight="700" fill="#fff">01</text></svg>
    <h3>QUALITY GUARANTEE</h3>
    <p>StandingMend.com has gained recognition in the Internet Reputation industry by continually providing high-value services to our clients...<a href="#">ReadMore</a></p>
  </div>
  <div class="abs feature" style="top:873px">
    <svg width="100" height="100" viewBox="0 0 100 100"><circle cx="40" cy="56" r="36" fill="none" stroke="#e6eaee" stroke-width="3"/><path d="M40 20 A36 36 0 0 1 76 56" fill="none" stroke="#1A9BFC" stroke-width="4"/><circle cx="40" cy="56" r="27" fill="#fff" stroke="#dde2e6"/><g fill="#1C3344"><circle cx="28" cy="50" r="5"/><circle cx="40" cy="46" r="6"/><circle cx="52" cy="50" r="5"/><rect x="23" y="57" width="10" height="12" rx="3"/><rect x="34" y="54" width="12" height="16" rx="3"/><rect x="47" y="57" width="10" height="12" rx="3"/></g><circle cx="76" cy="14" r="13" fill="#1A9BFC"/><text x="76" y="18.5" text-anchor="middle" font-family="Open Sans,sans-serif" font-size="12" font-weight="700" fill="#fff">02</text></svg>
    <h3>LEADERSHIP</h3>
    <p>Our Company will incorporate the highest standards of practice in all of our activities, from customer care and technical support, to development...<a href="#">ReadMore</a></p>
  </div>
  <div class="abs feature" style="top:1011px">
    <svg width="100" height="100" viewBox="0 0 100 100"><circle cx="40" cy="56" r="36" fill="none" stroke="#e6eaee" stroke-width="3"/><path d="M40 20 A36 36 0 0 1 76 56" fill="none" stroke="#1A9BFC" stroke-width="4"/><circle cx="40" cy="56" r="27" fill="#fff" stroke="#dde2e6"/><circle cx="40" cy="52" r="12" fill="#1C3344"/><rect x="35" y="63" width="10" height="8" fill="#1C3344"/><circle cx="40" cy="52" r="4" fill="#fff"/><circle cx="76" cy="14" r="13" fill="#1A9BFC"/><text x="76" y="18.5" text-anchor="middle" font-family="Open Sans,sans-serif" font-size="12" font-weight="700" fill="#fff">03</text></svg>
    <h3>INNOVATION</h3>
    <p>StandingMend.com has gained status as a leading global Internet Reputation company. Our desire to satisfy our clients' requirements drives...<a href="#">ReadMore</a></p>
  </div>
</section>

<section class="services">
  <h2 class="abs section-title">OUR SERVICES</h2>
  <div class="abs services-divider"></div>
  <article class="abs service-card" style="left:165px">
    <div class="service-photo photo-personal" role="img" aria-label="Smiling woman working at a laptop in a bright office"></div>
    <h3>PERSONAL SERVICE</h3><div class="rule"></div>
    <p>Many people, from students to CEOs and other professionals, underestimate the harmful effect that poor...</p>
    <a class="btn-pill" href="#">READ MORE</a>
  </article>
  <article class="abs service-card" style="left:705px">
    <div class="service-photo photo-business" role="img" aria-label="Group of business people in suits standing together"></div>
    <h3>BUSINESS SERVICE</h3><div class="rule"></div>
    <p>Many companies, from small businesses to large corporations, underestimate the harmful effect that poor online...</p>
    <a class="btn-pill" href="#">READ MORE</a>
  </article>
</section>

<section class="signup">
  <h2 class="abs section-title signup-title">SIGN UP</h2>
  <div class="abs col-title" style="left:165px;top:1915px;width:330px">FOR THE BEST EXPERIENCE</div>
  <div class="abs col-title" style="left:705px;top:1915px;width:332px">OR, YOU CAN SIGNUP VIA EMAIL</div>
  <div class="abs signup-divider"></div>
  <span class="abs signup-or">OR</span>
  <a class="abs social-btn btn-hub" href="#"><span class="sq"></span>Sign up with SocialHub<span class="arrow">&gt;</span></a>
  <a class="abs social-btn btn-chirp" href="#"><span class="sq"></span>Sign up with ChirpLine<span class="arrow">&gt;</span></a>
  <div class="abs field" style="top:1971px">Email</div>
  <div class="abs field" style="top:2021px">Password</div>
  <div class="abs field" style="top:2071px">Confirm Password</div>
  <a class="abs btn-create" href="#">CREATE MY ACCOUNT</a>
  <p class="abs terms">By signing up you accept Standing Mend <a href="#">Terms of Service</a> and <a href="#">Privacy Policy</a>.</p>
</section>

<footer class="footer">
  <h4 style="left:73px">QUICK LINKS</h4>
  <ul style="left:73px"><li>Personal</li><li>Business</li><li>About Us</li><li>Account Login</li><li>Signup</li></ul>
  <h4 style="left:253px">SERVICES</h4>
  <ul style="left:253px"><li>Personal Service</li><li>Business Service</li></ul>
  <h4 style="left:433px">RESOURCES</h4>
  <ul style="left:433px"><li>Case Studies</li><li>Free Reputation Check</li><li>Reputation Advice</li><li>Videos</li></ul>
  <h4 style="left:613px">GET IN TOUCH</h4>
  <div class="contact" style="top:92px"><span class="ico"><svg width="12" height="16" viewBox="0 0 12 16"><path d="M6 0 C2.7 0 0 2.6 0 6 C0 10 6 16 6 16 C6 16 12 10 12 6 C12 2.6 9.3 0 6 0Z" fill="#fff"/><circle cx="6" cy="6" r="2.2" fill="#3a5366"/></svg></span><span>228, Lorem ipsum dolor<br>sit aremt sor- 859584</span></div>
  <div class="contact" style="top:148px"><span class="ico"><svg width="14" height="14" viewBox="0 0 28 28"><path d="M7 3 L11 9 L8 12 C10 16 12 18 16 20 L19 17 L25 21 L22 26 C12 25 3 16 2 6 Z" fill="#fff"/></svg></span><span>Phone :<br>(+44) 01632 960418</span></div>
  <div class="contact" style="top:204px"><span class="ico"><svg width="14" height="11" viewBox="0 0 38 30"><rect x="1" y="3" width="36" height="25" fill="none" stroke="#fff" stroke-width="4"/><path d="M2 5 L19 18 L36 5" fill="none" stroke="#fff" stroke-width="4"/></svg></span><span>Email :<br>info@standingmend.com</span></div>
  <h4 style="left:883px">STAY CONNECTED</h4>
  <div class="follow" style="top:90px"><span class="ring"></span>Follow Us On SocialHub</div>
  <div class="follow" style="top:135px"><span class="ring"></span>Follow Us On ChirpLine</div>
  <div class="follow" style="top:180px"><span class="ring"></span>Follow Us On WorkLinks</div>
  <div class="subfooter">
    <span class="copy">Copyright 2015 StandingMend.com</span>
    <nav><a href="#">Become A Partner</a><a href="#">Company</a><a href="#">FAQ'S</a><a href="#">Our Team</a><a href="#">Privacy Policy</a><a href="#">TOS</a></nav>
  </div>
</footer>

</body>
</html>
```